Startup Drone Platform Company business card

We are needing a business card design for our employees. We are a startup drone platform. We are looking for a business card that has our logo on one side, with the employee/company details on the opposite side. We are looking for something that is very eye catching, modern, and bold.

Target Market(s)

This will target both drone pilots and drone businesses, along with all the industries that could utilize drone services (aerial video, aerial photos, inspections, 3d mapping, etc).

Industry/Entity Type

Business

```html
<!DOCTYPE html>
<html lang="en">
<head>
<meta charset="utf-8">
<title>Skylane Rent – Business Card</title>
<link href="https://fonts.googleapis.com/css2?family=Open+Sans:wght@400;600;700&display=swap" rel="stylesheet">
<style>
  :root {
    --stage: #e7e5e0;
    --card-black: #050505;
    --teal-light: #62dde4;
    --teal-dark: #38bcc6;
    --ink: #10191b;
    --strip: #e9e9e9;
    --white: #ffffff;
    --accent: #3fd0da;
  }
  * { box-sizing: border-box; margin: 0; padding: 0; }
  html, body {
    width: 1200px; height: 780px; overflow: hidden;
    background: var(--stage);
    font-family: "Open Sans", Arial, sans-serif;
  }
  .stage {
    width: 1200px; height: 780px;
    display: flex; align-items: center; justify-content: center; gap: 40px;
  }
  .card {
    width: 540px; height: 309px;
    background: var(--card-black);
    box-shadow: 0 10px 24px rgba(0,0,0,.22);
    position: relative; overflow: hidden;
  }

  /* shared wordmark */
  .wordmark {
    display: flex; align-items: center; justify-content: center;
    color: var(--white); font-weight: 400; text-transform: uppercase;
    white-space: nowrap;
  }
  .wordmark-dot {
    display: inline-block; border-radius: 50%;
    background: var(--accent);
  }

  /* front side */
  .front-top {
    height: 140px; display: flex; align-items: center; justify-content: center;
  }
  .front-top .wordmark { font-size: 28px; letter-spacing: 13px; gap: 10px; }
  .front-top .wordmark-dot { width: 16px; height: 16px; margin-right: 12px; }

  .details-band {
    height: 122px;
    background: linear-gradient(90deg, var(--teal-dark), var(--teal-light) 55%, var(--teal-dark));
    display: flex; align-items: center; padding: 0 34px;
    color: var(--ink);
  }
  .person { display: flex; flex-direction: column; align-items: flex-end; padding-right: 22px; }
  .person-name { font-weight: 700; font-size: 20px; letter-spacing: .2px; }
  .person-role { font-size: 15px; margin-top: 0; }
  .divider { width: 1.5px; height: 62px; background: var(--ink); }
  .contacts { list-style: none; padding-left: 18px; font-size: 14px; line-height: 23px; }
  .contacts li { display: flex; align-items: center; gap: 9px; }
  .contacts svg { width: 14px; height: 14px; flex: none; }

  .address-strip {
    height: 47px; background: var(--strip);
    display: flex; align-items: center; padding-left: 34px;
    font-size: 16px; color: var(--ink);
  }

  /* back side */
  .back { display: flex; align-items: center; justify-content: center; }
  .back .wordmark { font-size: 32px; letter-spacing: 16px; gap: 12px; }
  .back .wordmark-dot { width: 18px; height: 18px; margin-right: 14px; }
</style>
</head>
<body>
<main class="stage">

  <section class="card card-front" aria-label="Business card front">
    <header class="front-top">
      <div class="wordmark">
        <span>Skylane</span><span class="wordmark-dot"></span><span>Rent</span>
      </div>
    </header>

    <div class="details-band">
      <div class="person">
        <span class="person-name">EMPLOYEE NAME</span>
        <span class="person-role">Director</span>
      </div>
      <span class="divider"></span>
      <ul class="contacts">
        <li>
          <svg viewBox="0 0 16 16" aria-hidden="true"><path fill="#10191b" d="M3.5 1.5l2.2 2.6-1.3 1.5c.9 2.1 2.6 3.8 4.8 4.9l1.5-1.3 2.7 2.2-1.3 2.3C6.9 13.5 2.4 9 1.2 2.8z"/></svg>
          <span>0123 456 789</span>
        </li>
        <li>
          <svg viewBox="0 0 16 16" aria-hidden="true"><rect x="1" y="3" width="14" height="10" fill="#10191b"/><path d="M1.5 3.5L8 9l6.5-5.5" fill="none" stroke="#5bd6de" stroke-width="1.3"/></svg>
          <span>info@youremail.com</span>
        </li>
        <li>
          <svg viewBox="0 0 16 16" aria-hidden="true"><g fill="none" stroke="#10191b" stroke-width="1.3"><circle cx="8" cy="8" r="6.5"/><ellipse cx="8" cy="8" rx="2.8" ry="6.5"/><path d="M1.5 8h13M2.6 4.6h10.8M2.6 11.4h10.8"/></g></svg>
          <span>www.yoursite.com</span>
        </li>
      </ul>
    </div>

    <footer class="address-strip">
      <span>Your Adress Inc 2nd Lane Ave Milltown, ST 00000</span>
    </footer>
  </section>

  <section class="card card-back back" aria-label="Business card back">
    <div class="wordmark">
      <span>Skylane</span><span class="wordmark-dot"></span><span>Rent</span>
    </div>
  </section>

</main>
</body>
</html>
```